Medicaid and Nursing Home Planning Law Firm Needs Customizable Flyer

We need a flyer for The Delvecko Law Firm, P.C. that incorporates our logo, color scheme and existing collaterals (see uploads) and that can be easily updated. The flyer could advertise an upcoming speech/seminar/gathering, but the text should be customizable so that we can revise it later on using either MSWord or some other basic software.

Industry/Entity Type

Legal

Requirements
Must have
• Logo and contact information for business, including address, phone number, email and website information
Nice to have
• Also should advertise our 2nd location: 418 Pembury Avenue, Suite 307, Watertown, NY 13607

```html
<!DOCTYPE html>
<html lang="en">
<head>
<meta charset="utf-8">
<title>The Delvecko Law Firm, P.C. — Flyer</title>
<link rel="stylesheet" href="https://fonts.googleapis.com/css2?family=Open+Sans:wght@300;400;600&display=swap">
<style>
  :root {
    --orange: #d97a2f;
    --orange-deep: #c8692a;
    --band-dark: #5a2f1c;
    --ink: #1e1e1e;
    --white: #ffffff;
    --rule: rgba(255,255,255,0.45);
  }
  * { margin: 0; padding: 0; box-sizing: border-box; }
  html, body { width: 848px; height: 1200px; overflow: hidden; background: var(--white); }
  body { font-family: "Open Sans", Arial, sans-serif; }
  .flyer { position: relative; width: 848px; height: 1200px; overflow: hidden; }

  .hero-photo {
    position: absolute; left: 0; top: 0; width: 848px; height: 566px;
    background:
      linear-gradient(180deg, rgba(0,0,0,0) 0%, rgba(0,0,0,0) 61%, rgba(60,25,10,0.35) 61%, rgba(60,25,10,0.45) 100%),
      radial-gradient(ellipse at 20% 22%, #fff3c8 0%, #f4b55a 18%, #c9732d 42%, #7a3a1c 75%, #4a2416 100%);
  }
  .brand {
    position: absolute; left: 48px; top: 72px;
    display: flex; align-items: center; gap: 12px;
    font-weight: 400; font-size: 19px; letter-spacing: 1.5px;
    color: var(--orange); text-transform: uppercase;
  }
  .brand-mark { width: 14px; height: 14px; background: var(--orange); }

  .message {
    position: absolute; left: 0; top: 566px; width: 848px; height: 369px;
    background: var(--orange);
    border-top: 14px solid var(--band-dark);
  }
  .headline {
    position: absolute; left: 71px; top: 46px;
    border-left: 6px solid var(--white);
    padding-left: 26px;
    color: var(--white); font-weight: 300; font-size: 46px; line-height: 57px;
    text-transform: uppercase; letter-spacing: -0.5px;
  }
  .rule { position: absolute; left: 0; width: 848px; height: 1px; background: var(--rule); }
  .rule-top { top: 242px; }
  .rule-bottom { top: 333px; }
  .practice {
    position: absolute; left: 71px; top: 257px; width: 740px;
    color: var(--white); font-size: 21.5px; line-height: 34px; font-weight: 400;
  }

  .footer-photo {
    position: absolute; left: 0; top: 935px; width: 540px; height: 265px;
    background: linear-gradient(180deg, #cbb9b2 0%, #bfaea9 40%, #a79894 100%);
  }
  .contact {
    position: absolute; left: 565px; top: 998px;
    color: var(--ink); font-size: 13.5px; line-height: 16px;
  }
  .contact p { margin-bottom: 22px; }
  .contact .lines p { margin-bottom: 0; }
  .website {
    position: absolute; left: 565px; top: 1156px;
    color: var(--orange); font-size: 13.5px; font-weight: 600; letter-spacing: 1.8px;
  }
</style>
</head>
<body>
<div class="flyer">
  <div class="hero-photo" role="img" aria-label="Older couple embracing in a golden field at sunset, seen from behind"></div>
  <div class="brand"><span class="brand-mark"></span>The Delvecko Law Firm, P.C.</div>

  <section class="message">
    <h1 class="headline">Protecting<br>everything that<br>matters to you.</h1>
    <div class="rule rule-top"></div>
    <p class="practice">New York’s Elder Law, Medicaid, Estate Planning, Trust &amp; Estate Litigation, Guardianship And Special Needs Planning Law Firm.</p>
    <div class="rule rule-bottom"></div>
  </section>

  <div class="footer-photo" role="img" aria-label="Soft blurred field in muted pink and grey tones"></div>

  <address class="contact" style="font-style:normal">
    <p>2730 Hollister Lane<br>East Syracuse, New York 13059</p>
    <p>418 Pembury Avenue,<br>Suite 307, Watertown, NY 13607</p>
    <div class="lines">
      <p>Office: (315) 555-0147</p>
      <p>Email: info@thedelveckolawfirm.com</p>
    </div>
  </address>
  <div class="website">www.thedelveckolawfirm.com</div>
</div>
</body>
</html>
```